The next stage in our 106 year history in Specialised Stationery

We need a business card design(which is also adaptable for our general stationery) to suit the changing face of our business. Harlow, an Australian company has been the leader in its category since 1907. We design and print various books required by small business to comply with government legislation in regards to keeping records. Accountancy, Payroll, Vehicle usage recording, Firearms registration etc. The Harlow logo a blue diamond is one of the best known in our industry. As manual recording has declined in the last few years we have diversified into other areas: Safety Apparel, Personal Protective Equipment (PPE) and web based software for bookkeeping and Customer Relationship management(CRM). Separate logos have been adopted for each of these being: Harlow Systems, Harlow Safety, Harlow Apparel and Harlow Software each with same diamond but different colour background. This has made it easy to identify the different sectors but difficult to bring together for a Corporate identity in Business cards etc. We are looking to bring all logos together (not one logo) but still allow the logo to depict the diversity of our offering, while still being able to have a category specific logo for each of the divisions. All products go through the same distribution channel, Office Products. The final design should depict an old established company well, known and trusted but leaping forward and still retaining same values they have come to trust.

Target Market(s)

Micro to small business companies generally who employ 20 or less people.

Industry/Entity Type

Small Business

Requirements
Must have
• The diamonds are well recognised and the new design should retain the integrity of them.

```html
<!DOCTYPE html>
<html lang="en">
<head>
<meta charset="utf-8">
<title>Harlow Business Card</title>
<link rel="stylesheet" href="https://fonts.googleapis.com/css2?family=Open+Sans:wght@400;600;700&display=swap">
<style>
  :root {
    --stage: #ece9e4;
    --blue-light: #2a8fd6;
    --blue: #1470bd;
    --blue-deep: #0a5a9e;
    --card-white: #ffffff;
    --card-grey: #e4e6e8;
    --edge-grey: #b9bcc0;
    --text-grey: #5d6166;
    --icon-blue: #1a6fb8;
    --systems: #2a7fcf;
    --software: #c8283a;
    --apparel: #3da63a;
    --safety: #e2582c;
    --white: #ffffff;
  }
  * { box-sizing: border-box; margin: 0; padding: 0; }
  html, body {
    width: 1200px; height: 675px; overflow: hidden;
    background: var(--stage);
    font-family: "Open Sans", Arial, sans-serif;
  }
  .stage { position: relative; width: 1200px; height: 675px; }
  .card {
    position: absolute; top: 183px;
    width: 540px; height: 309px;
    overflow: hidden;
    box-shadow: 0 6px 18px rgba(0,0,0,0.18);
  }

  /* Front */
  .card-front {
    left: 40px;
    background: radial-gradient(ellipse at 42% 38%, var(--blue-light) 0%, var(--blue) 50%, var(--blue-deep) 100%);
  }
  .division {
    position: absolute;
    display: flex; align-items: center; gap: 7px;
    color: var(--white);
    font-size: 12px; font-weight: 700; letter-spacing: 0.3px;
    white-space: nowrap;
  }
  .division-swatch { width: 14px; height: 14px; border: 2px solid var(--white); }
  .division-systems { left: 118px; top: 62px; }
  .division-systems .division-swatch { background: var(--systems); }
  .division-software { left: 196px; top: 100px; }
  .division-software .division-swatch { background: var(--software); }
  .division-apparel { left: 276px; top: 138px; }
  .division-apparel .division-swatch { background: var(--apparel); }
  .division-safety { left: 356px; top: 176px; }
  .division-safety .division-swatch { background: var(--safety); }
  .front-url {
    position: absolute; left: 176px; top: 236px;
    color: var(--white); font-size: 13px;
  }

  /* Back */
  .card-back {
    left: 620px;
    background: linear-gradient(160deg, var(--card-white) 0%, var(--card-white) 40%, var(--card-grey) 100%);
  }
  .back-art { position: absolute; inset: 0; }
  .brand {
    position: absolute; left: 52px; top: 34px;
    display: flex; align-items: center; gap: 9px;
    color: var(--blue); font-size: 24px; font-weight: 700; letter-spacing: 0.5px;
  }
  .brand-swatch { width: 18px; height: 18px; background: var(--blue); }
  .company {
    position: absolute; left: 52px; top: 96px;
    color: var(--text-grey); font-size: 11.5px; line-height: 16px;
  }
  .contact-list {
    position: absolute; left: 52px; top: 152px;
    list-style: none;
    color: var(--text-grey); font-size: 11.5px; line-height: 17px;
  }
  .contact-list li { display: flex; align-items: center; gap: 7px; }
  .contact-list svg { width: 10px; height: 10px; fill: var(--icon-blue); flex: none; }
  .holder {
    position: absolute; right: 34px; top: 222px;
    text-align: right; color: var(--white);
  }
  .holder-name { font-size: 16px; font-weight: 400; }
  .holder-role { font-size: 11.5px; margin-top: 1px; }
</style>
</head>
<body>
<main class="stage">

  <section class="card card-front" aria-label="Card front">
    <div class="division division-systems"><span class="division-swatch"></span>Harlow Systems</div>
    <div class="division division-software"><span class="division-swatch"></span>Harlow Software</div>
    <div class="division division-apparel"><span class="division-swatch"></span>Harlow Apparel</div>
    <div class="division division-safety"><span class="division-swatch"></span>Harlow Safety</div>
    <p class="front-url">www.harlow.com.au</p>
  </section>

  <section class="card card-back" aria-label="Card back">
    <svg class="back-art" viewBox="0 0 540 309" preserveAspectRatio="none" aria-hidden="true">
      <polygon points="250,164 540,100 540,309 348,309" fill="var(--edge-grey)"/>
      <polygon points="262,162 540,104 540,309 358,309" fill="var(--blue)"/>
    </svg>

    <div class="brand"><span class="brand-swatch"></span>Harlow</div>

    <p class="company">Harlow Pty Limited<br>Unit 4, 218 Kestrel Road,<br>Marlow Bay, NSW 2231</p>

    <ul class="contact-list">
      <li><svg viewBox="0 0 10 10"><path d="M2 0.5 L4 2.5 L3 4 Q4.5 6 6 7 L7.5 6 L9.5 8 L8 9.5 Q3 9 0.5 2 Z"/></svg>61 2 9400 3185</li>
      <li><svg viewBox="0 0 10 10"><rect x="2.5" y="0" width="5" height="10" rx="1"/></svg>0400 512 377</li>
      <li><svg viewBox="0 0 10 10"><rect x="0" y="4" width="10" height="5" rx="1"/><rect x="2" y="0.5" width="6" height="3"/></svg>61 2 9400 3186</li>
      <li><svg viewBox="0 0 10 10"><rect x="0" y="2" width="10" height="7" rx="1"/></svg>info@harlow.com.au</li>
      <li><svg viewBox="0 0 10 10"><circle cx="5" cy="5" r="5"/></svg>www.harlow.com.au</li>
    </ul>

    <div class="holder">
      <p class="holder-name">Peter Langford</p>
      <p class="holder-role">Managing Director</p>
    </div>
  </section>

</main>
</body>
</html>
```